Consulting Firm of Business Savvy Super Geeks Needs Business Cards Redesigned

We need our business cards redesigned to reflect the company branding better, especially the website: www.TrelvoConsulting.com . Note the phrase "Business Savvy. Technology Smart" from the website. Also would love to see options that include verbiage of our offerings: Cloud Solutions, Digital Workspace, CRM Services, Dravelin Partner, Security Services, ERP Services.

Industry/Entity Type

Consulting

Contact Information for Business Card

Direct Phone #, Cell Phone #, Linkedin Address, Web address, Office Address

Font styles to use
Sans Serif

Requirements
Must have
• The cards should reflect the website.
• Clean design.
Nice to have
• Mentions to each of the business units / practices mentioned in the description.

```html
<!DOCTYPE html>
<html lang="en">
<head>
<meta charset="utf-8">
<title>Trelvo Consulting – Business Cards</title>
<link rel="stylesheet" href="https://fonts.googleapis.com/css2?family=Roboto:wght@400;500;700&family=Roboto+Condensed:wght@700&display=swap">
<style>
  :root {
    --bg: #2b2d30;
    --slate: #44535f;
    --ink: #3f4f5c;
    --blue: #1a86d0;
    --blue-light: #4db8ea;
    --paper: #f7f8f8;
    --white: #ffffff;
    --muted: #5a6268;
  }
  * { box-sizing: border-box; margin: 0; padding: 0; }
  html, body { width: 1200px; height: 886px; overflow: hidden; }
  body {
    background: var(--bg);
    font-family: "Roboto", Arial, sans-serif;
    position: relative;
  }
  .card {
    position: absolute;
    width: 540px;
    height: 309px;
    border-radius: 2px;
    box-shadow: 0 10px 30px rgba(0,0,0,.45);
    overflow: hidden;
  }
  /* Back of card */
  .card-back {
    left: 40px; top: 289px;
    background: var(--slate);
    color: var(--white);
    text-align: center;
  }
  .back-brand {
    margin-top: 58px;
    display: inline-flex; align-items: center; gap: 10px;
    font-weight: 700; font-size: 34px; color: var(--blue-light);
  }
  .brand-square { width: 22px; height: 22px; background: var(--blue); display: inline-block; flex: none; }
  .back-rule { width: 420px; height: 1px; background: rgba(255,255,255,.75); margin: 0 auto; }
  .back-rule.top { margin-top: 26px; }
  .services-title {
    margin-top: 12px;
    color: var(--blue); font-weight: 500; font-size: 15px; letter-spacing: .5px;
  }
  .services-list { font-size: 12.5px; line-height: 19px; margin-top: 4px; }
  .services-list .sep { color: var(--blue-light); padding: 0 4px; }
  .tagline {
    color: var(--blue); font-weight: 500; font-size: 15px; margin: 6px 0 10px;
  }
  /* Front of card */
  .card-front {
    left: 620px; top: 289px;
    background: var(--paper);
    color: var(--muted);
  }
  .person {
    position: absolute; right: 40px; top: 30px; text-align: right;
  }
  .person-name {
    font-family: "Roboto Condensed", Arial, sans-serif;
    font-weight: 700; font-size: 21px; color: var(--blue); letter-spacing: .3px;
  }
  .person-role { font-size: 13px; color: var(--ink); margin-top: 1px; }
  .person-email { font-size: 11.5px; margin-top: 6px; }
  .front-brand {
    position: absolute; left: 34px; top: 70px;
    display: flex; align-items: flex-start; gap: 10px;
  }
  .front-brand .brand-name {
    font-weight: 700; font-size: 34px; line-height: 34px; color: var(--ink);
  }
  .front-brand .brand-square { margin-top: 6px; }
  .address {
    position: absolute; left: 36px; top: 158px;
    font-size: 12.5px; line-height: 16px;
  }
  .contacts {
    position: absolute; left: 36px; top: 200px;
    list-style: none; font-size: 12.5px; line-height: 17px;
  }
  .contacts li { display: flex; align-items: center; gap: 7px; }
  .contacts svg { width: 11px; height: 11px; flex: none; }
</style>
</head>
<body>

<section class="card card-back" aria-label="Card back">
  <div class="back-brand"><span class="brand-square"></span>Trelvo</div>
  <div class="back-rule top"></div>
  <h2 class="services-title">SERVICES</h2>
  <p class="services-list">
    Cloud Solutions<span class="sep">·</span>Digital Workspace<br>
    CRM Services<span class="sep">·</span>Dravelin Partner<span class="sep">·</span>Security Services<span class="sep">·</span>ERP Services.
  </p>
  <p class="tagline">Business Savvy. Technology Smart</p>
  <div class="back-rule"></div>
</section>

<section class="card card-front" aria-label="Card front">
  <div class="person">
    <div class="person-name">DAREN HOLT</div>
    <div class="person-role">CEO</div>
    <div class="person-email">daren.holt@trelvoconsulting.com</div>
  </div>

  <div class="front-brand">
    <div class="brand-name">Trelvo<br>Consulting</div>
    <span class="brand-square"></span>
  </div>

  <p class="address">Riverton HQ, 218 Alder Street<br>Marlow, PA 15990</p>

  <ul class="contacts">
    <li>
      <svg viewBox="0 0 12 12"><path d="M3 1 L5 3.5 L4 5 Q5 7 7 8 L8.5 7 L11 9 L9.5 11 Q4 10.5 1 3 Z" fill="var(--blue)"/></svg>
      555-314-7720
    </li>
    <li>
      <svg viewBox="0 0 12 12"><path d="M3 1 L5 3.5 L4 5 Q5 7 7 8 L8.5 7 L11 9 L9.5 11 Q4 10.5 1 3 Z" fill="var(--blue)"/></svg>
      555-962-4051
    </li>
    <li>
      <svg viewBox="0 0 12 12"><rect x="3" y="0.8" width="6" height="10.4" rx="1" fill="none" stroke="var(--blue)" stroke-width="1.4"/></svg>
      555-473-8195
    </li>
    <li>
      <svg viewBox="0 0 12 12"><rect x="1" y="1" width="10" height="10" fill="var(--blue)"/></svg>
      trelvo-consulting
    </li>
    <li>
      <svg viewBox="0 0 12 12"><circle cx="6" cy="6" r="5" fill="var(--blue)"/><path d="M1 6 H11 M6 1 Q3 6 6 11 M6 1 Q9 6 6 11" stroke="var(--paper)" stroke-width=".8" fill="none"/></svg>
      www.TrelvoConsulting.com
    </li>
  </ul>
</section>

</body>
</html>
```